Hispanic Financial Counseling and Advocate Firm seeks business card design

Looking for a clean, professional business card design. This is a firm that specializes in providing financial education, coaching, and planning to the Hispanic community. The name of the company is Valemar, which means to prosper. We need a design that is clean, professional, and invokes trust, professionalism, but also welcoming. Our logo is a plant growing from a hand to give the messaging of of being in control of growing your financial future and security. Its part of a larger organization names Celesta Financial Group, who's logo is a tree with multi colored branches. We have the back of the card designed so we just need the front designed. the back is blue, so front needs to be a different background color, not blue.

Target Market(s)

Hispanic Community looking to better their future

Industry/Entity Type

financial services

Contact Information for Business Card

contact info: Anselmo Ibarra Jr, 951-555-0147, info@celestafinancialgroup.example. Celestafinancialgroup.example. tag line: Para un futuro mas seguro!

Requirements
Must have
• basics: logo, contact info.
Nice to have
• possibly incorporate the tree logo provided somehow
Should not have
• should not look like the back, needs to be different from the back provided.

```html
<!DOCTYPE html>
<html lang="es">
<head>
<meta charset="utf-8">
<title>Valemar – Business Card</title>
<link href="https://fonts.googleapis.com/css2?family=Arimo:wght@400;700&family=Montserrat:wght@500;600;700&display=swap" rel="stylesheet">
<style>
  :root {
    --page: #e4e4e4;
    --slate: #4b5874;
    --navy: #002f45;
    --leaf: #6aa842;
    --white: #ffffff;
    --dot-green: #9cc43b;
    --dot-blue: #2aa7df;
    --dot-red: #ef4b55;
    --dot-purple: #a489c4;
    --dot-yellow: #f6c21c;
  }
  * { margin: 0; padding: 0; box-sizing: border-box; }
  html, body { width: 1200px; height: 1200px; overflow: hidden; }
  body { background: var(--page); position: relative; font-family: "Arimo", Arial, sans-serif; }

  .card { position: absolute; left: 266px; width: 667px; height: 392px; overflow: hidden; }
  .card--front { top: 166px; background: var(--slate); }
  .card--back { top: 589px; background: var(--navy); font-family: "Montserrat", Arial, sans-serif; }

  /* Front */
  .brand-mark { position: absolute; left: 38px; top: 48px; width: 58px; height: 58px; border-radius: 50%; background: var(--leaf); }
  .brand-name { position: absolute; left: 128px; top: 47px; font-family: "Montserrat", Arial, sans-serif; font-weight: 600; font-size: 46px; line-height: 1; color: var(--leaf); letter-spacing: -0.5px; }
  .brand-sub { position: absolute; left: 130px; top: 101px; font-family: "Montserrat", Arial, sans-serif; font-weight: 700; font-size: 12.5px; letter-spacing: 2px; color: var(--white); }

  .person { position: absolute; left: 33px; top: 182px; }
  .person__name { font-weight: 700; font-size: 24px; color: var(--white); line-height: 1.1; }
  .person__role { font-size: 17px; color: var(--leaf); margin-top: 4px; }

  .contact { position: absolute; left: 36px; top: 248px; list-style: none; }
  .contact li { display: flex; align-items: center; gap: 4px; height: 22px; font-size: 16px; color: var(--white); }
  .contact svg { width: 11px; height: 11px; flex: none; }

  .tagline-band { position: absolute; left: 0; top: 329px; width: 380px; height: 31px; }
  .tagline { position: absolute; left: 33px; top: 336px; font-weight: 700; font-size: 16px; color: var(--white); }

  /* Back */
  .group-mark { position: absolute; left: 72px; top: 70px; width: 140px; height: 140px; border-radius: 50%; background: var(--dot-blue); }
  .divider { position: absolute; left: 252px; top: 29px; width: 2px; height: 215px; background: var(--white); }
  .group-name { position: absolute; left: 284px; top: 92px; color: var(--white); font-weight: 600; line-height: 1; }
  .group-name__main { display: block; font-size: 84px; letter-spacing: -3px; }
  .group-name__sub { display: block; font-size: 28px; margin-top: 4px; letter-spacing: 0.5px; }

  .services { position: absolute; left: 0; right: 0; top: 298px; text-align: center; color: var(--white); font-size: 20px; font-weight: 500; line-height: 26px; }
  .service { white-space: nowrap; margin: 0 5px; }
  .service::before { content: ""; display: inline-block; width: 9px; height: 9px; border-radius: 50%; margin-right: 6px; vertical-align: 2px; background: var(--c); }
</style>
</head>
<body>

<section class="card card--front" aria-label="Front of card">
  <span class="brand-mark" aria-hidden="true"></span>
  <div class="brand-name">Valemar</div>
  <div class="brand-sub">SERVICIOS FINANCIEROS</div>

  <div class="person">
    <div class="person__name">Anselmo Ibarra Jr</div>
    <div class="person__role">Founder</div>
  </div>

  <ul class="contact">
    <li>
      <svg viewBox="0 0 12 12" aria-hidden="true"><path fill="#6aa842" d="M2.4 0.6l2 2.2-1 1.2c.6 1.5 1.8 2.7 3.3 3.4l1.2-1 2.3 2-1 2C5 10.3 1.6 7 .6 2.2z"/></svg>
      951-555-0147
    </li>
    <li>
      <svg viewBox="0 0 12 12" aria-hidden="true"><rect x="0.5" y="2.5" width="11" height="7" fill="#6aa842"/><path d="M0.5 2.5L6 6.5l5.5-4" stroke="#4b5874" stroke-width="1" fill="none"/></svg>
      info@celestafinancialgroup.example
    </li>
    <li>
      <svg viewBox="0 0 12 12" aria-hidden="true"><g fill="none" stroke="#6aa842" stroke-width="1"><circle cx="6" cy="6" r="5"/><ellipse cx="6" cy="6" rx="2.2" ry="5"/><path d="M1 6h10M2 3.5h8M2 8.5h8"/></g></svg>
      Celestafinancialgroup.example
    </li>
  </ul>

  <svg class="tagline-band" viewBox="0 0 380 31" aria-hidden="true"><polygon points="0,0 314,0 371,31 0,31" fill="#6aa842"/></svg>
  <div class="tagline">Para un futuro mas seguro!</div>
</section>

<section class="card card--back" aria-label="Back of card">
  <span class="group-mark" aria-hidden="true"></span>
  <span class="divider" aria-hidden="true"></span>
  <div class="group-name">
    <span class="group-name__main">Celesta</span>
    <span class="group-name__sub">Financial Group Inc</span>
  </div>

  <div class="services">
    <div><span class="service" style="--c: var(--dot-green)">Inmigración</span> <span class="service" style="--c: var(--dot-blue)">Planificacion Financiera</span></div>
    <div><span class="service" style="--c: var(--dot-red)">Seguros</span> <span class="service" style="--c: var(--dot-purple)">Impuestos</span> <span class="service" style="--c: var(--dot-red)">Y mas</span></div>
    <div><span class="service" style="--c: var(--dot-yellow)">Preparación de documentos</span></div>
  </div>
</section>

</body>
</html>
```